SaaS startup seeking website design and build on Hovrix.io

Need a website designed and built on Hovrix.io for a new SaaS startup called TenaPod (logo provided).

***The winning designer will be provided with a login to our Hovrix.io subscription to deploy the design - please only submit a design if you are familiar with the Hovrix platform. ***

The business will be selling a cloud-based system for customer success management; a tool to ensure SaaS businesses successfully onboard, retain for renewals, upsell and cross-sell to existing customers. Logo and colour guide provided, pages required in the design:
Home,
Tour,
Pricing,
Blog,
Contact

Require buttons/ forms for
Login,
Sign-up for Trial,
Sign-up for Newsletter,
Request Demo,
Contact Us.

The winning designer will be provided with a login to our Hovrix.io subscription to deploy the design - please only submit a design if you are familiar with the Hovrix platform. Draft designs submitted on trial hovrix accounts will also be considered.

Seek inspiration and placeholder content from https://flexmoria.net/
https://www.quibarra.com/
https://palvenrow.com/

Target Market(s)

SaaS companies

Coding

Coded - Design and coding required

Number of Pages Required

1 page

```html
<!DOCTYPE html>
<html lang="en">
<head>
<meta charset="utf-8">
<title>TenaPod – Customer success management</title>
<link rel="stylesheet" href="https://fonts.googleapis.com/css2?family=Open+Sans:wght@400;600;700&display=swap">
<style>
  :root {
    --navy: #2b4a78;
    --navy-deep: #284470;
    --hero-a: #2a4c7d;
    --hero-b: #3a7fb8;
    --sky: #3b93d3;
    --sky-soft: #d3e6f3;
    --icon-bg: #d6e8f5;
    --ink: #333a45;
    --muted: #6b7480;
    --rule: #e3e6ea;
    --footer: #dcdcdc;
    --white: #ffffff;
  }
  * { box-sizing: border-box; margin: 0; padding: 0; }
  html, body { width: 1200px; height: 4622px; overflow: hidden; }
  body { font-family: "Open Sans", Arial, sans-serif; color: var(--ink); background: var(--white); }
  .page { position: relative; width: 1200px; height: 4622px; overflow: hidden; }
  .abs { position: absolute; }
  .bands { position: absolute; inset: 0; }

  /* nav */
  .brand { left: 144px; top: 8px; font-size: 36px; font-weight: 600; color: var(--navy); display: flex; align-items: center; gap: 10px; line-height: 44px; }
  .brand-dot { width: 26px; height: 26px; border-radius: 50%; background: var(--sky); }
  .nav-link { top: 20px; font-size: 15px; color: var(--navy); }
  .nav-btn { top: 12px; height: 40px; border-radius: 20px; color: var(--white); font-size: 13px; font-weight: 600; display: flex; align-items: center; justify-content: center; }

  /* hero */
  .hero-title { left: 144px; top: 190px; width: 430px; font-size: 33px; line-height: 43px; font-weight: 700; color: var(--white); }
  .hero-sub { left: 144px; top: 328px; width: 420px; font-size: 15px; line-height: 27px; color: #e4edf7; }
  .hero-form { left: 144px; top: 398px; width: 400px; height: 47px; border-radius: 24px; background: var(--white); border: 3px solid var(--white); display: flex; align-items: center; justify-content: space-between; padding-left: 20px; }
  .hero-form span { color: #7d8590; font-size: 16px; }
  .hero-form b { background: var(--sky); color: var(--white); height: 41px; width: 142px; border-radius: 21px; font-size: 15px; font-weight: 600; display: flex; align-items: center; justify-content: center; }
  .laptop-screen { left: 660px; top: 197px; width: 358px; height: 232px; background: #111; border-radius: 10px; padding: 9px; }
  .laptop-screen div { width: 100%; height: 100%; background: linear-gradient(180deg, #f4f6f9, #e6ebf1); }
  .laptop-base { left: 624px; top: 429px; width: 432px; height: 14px; background: linear-gradient(180deg, #d9dce0, #9ea3a9); border-radius: 0 0 14px 14px; }

  /* press row */
  .press { top: 755px; font-size: 26px; font-weight: 600; color: #5d6268; }
  .divider { left: 0; top: 869px; width: 1200px; height: 1px; background: var(--rule); }

  /* features */
  .sec-title { font-size: 31px; font-weight: 700; color: var(--navy); }
  .sec-text { width: 420px; font-size: 15px; line-height: 27px; color: #4a525c; }
  .feat { width: 420px; display: flex; gap: 10px; }
  .feat-icon { width: 54px; height: 54px; flex: none; background: var(--icon-bg); display: flex; align-items: center; justify-content: center; }
  .feat-icon svg { width: 24px; height: 24px; fill: var(--navy); }
  .feat h4 { font-size: 15px; font-weight: 700; color: #222; margin-top: -4px; margin-bottom: 6px; }
  .feat p { font-size: 11px; line-height: 19px; color: var(--muted); }
  .shot { background: var(--white); padding: 6px; box-shadow: 0 4px 14px rgba(30,50,80,.25); }
  .shot div { width: 100%; height: 100%; background: linear-gradient(90deg, #c9d3df 0 4%, #f3f5f8 4% 28%, #ffffff 28%); }

  /* pricing */
  .price-title { left: 0; width: 1200px; top: 2624px; text-align: center; font-size: 31px; font-weight: 700; color: var(--navy); }
  .price-sub { left: 0; width: 1200px; top: 2680px; text-align: center; font-size: 21px; color: #333; }
  .card { top: 2739px; width: 296px; height: 368px; background: var(--white); }
  .card h3 { position: absolute; top: 18px; width: 100%; text-align: center; font-size: 23px; font-weight: 600; color: var(--navy); }
  .card .blurb { position: absolute; top: 62px; left: 24px; right: 24px; text-align: center; font-size: 11px; line-height: 19px; color: var(--muted); }
  .card .price { position: absolute; top: 106px; width: 100%; text-align: center; color: var(--sky); font-size: 60px; font-weight: 700; line-height: 72px; }
  .card .price small { font-size: 22px; font-weight: 400; color: #666; }
  .card .rule { position: absolute; top: 192px; left: 0; right: 0; height: 1px; background: var(--rule); }
  .card ul { position: absolute; top: 212px; left: 18px; list-style: none; }
  .card li { font-size: 12px; line-height: 27px; color: #444; display: flex; align-items: center; gap: 8px; }
  .card li svg { width: 11px; height: 11px; fill: none; stroke: var(--sky); stroke-width: 3; }
  .card .btn { position: absolute; top: 307px; left: 20px; right: 20px; height: 40px; border-radius: 20px; background: var(--sky); color: var(--white); font-size: 13px; font-weight: 600; display: flex; align-items: center; justify-content: center; }

  /* contact */
  .contact-title { left: 0; width: 1200px; top: 3326px; text-align: center; font-size: 30px; font-weight: 700; color: #49a6e6; }
  .contact-sub { left: 0; width: 1200px; top: 3384px; text-align: center; font-size: 22px; color: #e9eef5; }
  .label { font-size: 15px; color: var(--white); }
  .field { background: var(--white); border: 1px solid #c9d3df; padding: 0 18px; display: flex; align-items: center; font-size: 15px; color: #7f8ea3; }
  .send { left: 524px; top: 3861px; width: 151px; height: 38px; border-radius: 19px; background: var(--sky); color: var(--white); font-size: 14px; font-weight: 600; display: flex; align-items: center; justify-content: center; }

  /* call to action */
  .cta-title { left: 0; width: 1200px; top: 4172px; text-align: center; font-size: 31px; font-weight: 700; color: var(--navy); }
  .cta-sub { left: 0; width: 1200px; top: 4230px; text-align: center; font-size: 22px; color: #333; }
  .cta-btn { top: 4230px; width: 159px; height: 48px; border-radius: 24px; color: var(--white); font-size: 15px; font-weight: 600; display: flex; align-items: center; justify-content: center; }

  /* footer */
  .foot-text { font-size: 13px; color: #444; }
  .social { top: 4535px; width: 18px; height: 18px; border-radius: 50%; background: #2a3038; }
</style>
</head>
<body>
<div class="page">

  <svg class="bands" width="1200" height="4622" viewBox="0 0 1200 4622" aria-hidden="true">
    <defs>
      <linearGradient id="heroGrad" x1="0" y1="0" x2="1" y2="0">
        <stop offset="0" stop-color="#2a4c7d"/>
        <stop offset="1" stop-color="#3a7fb8"/>
      </linearGradient>
    </defs>
    <polygon points="0,63 1200,63 1200,664 0,574" fill="url(#heroGrad)"/>
    <polygon points="0,2481 1200,2556 1200,3265 0,3184" fill="#d3e6f3"/>
    <polygon points="0,3184 1200,3265 1200,4054 0,3974" fill="#2b4a78"/>
    <polygon points="0,4342 1200,4422 1200,4622 0,4622" fill="#dcdcdc"/>
  </svg>

  <!-- navigation -->
  <header>
    <div class="abs brand"><span class="brand-dot"></span>tenapod</div>
    <a class="abs nav-link" style="left:626px">Features</a>
    <a class="abs nav-link" style="left:732px">Pricing</a>
    <a class="abs nav-link" style="left:823px">FAQ</a>
    <a class="abs nav-btn" style="left:888px;width:78px;background:var(--navy)">Login</a>
    <a class="abs nav-btn" style="left:976px;width:80px;background:var(--sky)">Sign Up</a>
  </header>

  <!-- hero -->
  <section>
    <h1 class="abs hero-title">Spark Interest: What makes your product desirable?</h1>
    <p class="abs hero-sub">Use this space to tell the customer how your product works and why it is different.</p>
    <div class="abs hero-form"><span>email@example.com</span><b>GET STARTED</b></div>
    <div class="abs laptop-screen"><div role="img" aria-label="Product dashboard screenshot on a laptop"></div></div>
    <div class="abs laptop-base"></div>
  </section>

  <!-- press -->
  <section aria-label="As seen in">
    <span class="abs press" style="left:144px">Founderly</span>
    <span class="abs press" style="left:376px">Marlowe</span>
    <span class="abs press" style="left:558px">PROSPERA</span>
    <span class="abs press" style="left:760px">Quill 500</span>
    <span class="abs press" style="left:900px;font-size:19px;line-height:22px;top:742px;text-align:center">THE<br>HALVERTON POST</span>
    <div class="abs divider"></div>
  </section>

  <!-- feature block 1 -->
  <section>
    <h2 class="abs sec-title" style="left:144px;top:942px">Aliquam erat volutpat</h2>
    <p class="abs sec-text" style="left:144px;top:992px">Nullam lorem urna, tempus eget mollis et, dapibus ac sem. Suspendisse gravida ornare pulvinar. Vestibulum luctus ex in egestas fringilla.</p>
    <div class="abs feat" style="left:144px;top:1106px"><div class="feat-icon"><svg viewBox="0 0 24 24"><path d="M3 20h18v2H3zM5 10h3v9H5zm5-5h3v14h-3zm5 8h3v6h-3z"/></svg></div><div><h4>Mauris bibendum</h4><p>Nulla in lorem at massa pellentesque posuere. Nulla tristique posuere molestie. Aliquam erat volutpat.</p></div></div>
    <div class="abs feat" style="left:144px;top:1202px"><div class="feat-icon"><svg viewBox="0 0 24 24"><path d="M12 22a2.5 2.5 0 0 0 2.5-2.5h-5A2.5 2.5 0 0 0 12 22zm7-6V11a7 7 0 0 0-5.5-6.8V3a1.5 1.5 0 0 0-3 0v1.2A7 7 0 0 0 5 11v5l-2 2v1h18v-1z"/></svg></div><div><h4>Duis ornare erat</h4><p>Nulla in lorem at massa pellentesque posuere. Nulla tristique posuere molestie. Aliquam erat volutpat.</p></div></div>
    <div class="abs feat" style="left:144px;top:1298px"><div class="feat-icon"><svg viewBox="0 0 24 24"><circle cx="12" cy="8" r="5"/><path d="M2 22c0-5 4.5-8 10-8s10 3 10 8z"/></svg></div><div><h4>Nam tempus</h4><p>Nulla in lorem at massa pellentesque posuere. Nulla tristique posuere molestie. Aliquam erat volutpat.</p></div></div>
    <div class="abs shot" style="left:615px;top:1032px;width:441px;height:242px"><div role="img" aria-label="Product import wizard screenshot"></div></div>
  </section>

  <!-- feature block 2 -->
  <section>
    <h2 class="abs sec-title" style="left:648px;top:1466px">Pellentesque blandit</h2>
    <p class="abs sec-text" style="left:648px;top:1516px">Nullam lorem urna, tempus eget mollis et, dapibus ac sem. Suspendisse gravida ornare pulvinar. Vestibulum luctus ex in egestas fringilla.</p>
    <div class="abs feat" style="left:648px;top:1630px"><div class="feat-icon"><svg viewBox="0 0 24 24"><path d="M2 20V4h2v14h18v2zm3-3 5-7 4 4 4-6 3 3v6z"/></svg></div><div><h4>Cras eget leo</h4><p>Nulla in lorem at massa pellentesque posuere. Nulla tristique posuere molestie. Aliquam erat volutpat.</p></div></div>
    <div class="abs feat" style="left:648px;top:1726px"><div class="feat-icon"><svg viewBox="0 0 24 24"><path d="M7 2h10a2 2 0 0 1 2 2v16a2 2 0 0 1-2 2H7a2 2 0 0 1-2-2V4a2 2 0 0 1 2-2zm0 3v13h10V5zm5 14.2a1 1 0 1 0 0 .1z"/></svg></div><div><h4>Praesent iaculis</h4><p>Nulla in lorem at massa pellentesque posuere. Nulla tristique posuere molestie. Aliquam erat volutpat.</p></div></div>
    <div class="abs feat" style="left:648px;top:1822px"><div class="feat-icon"><svg viewBox="0 0 24 24"><path d="M12 2 4 5v6c0 5 3.4 9.7 8 11 4.6-1.3 8-6 8-11V5zm0 3v15c-3.3-1.2-6-4.9-6-9V6.4z"/></svg></div><div><h4>Maecenas consequat</h4><p>Nulla in lorem at massa pellentesque posuere. Nulla tristique posuere molestie. Aliquam erat volutpat.</p></div></div>
    <div class="abs shot" style="left:144px;top:1557px;width:440px;height:237px"><div role="img" aria-label="Product import wizard screenshot"></div></div>
  </section>

  <!-- feature block 3 -->
  <section>
    <h2 class="abs sec-title" style="left:144px;top:1988px">Phasellus consequat</h2>
    <p class="abs sec-text" style="left:144px;top:2038px">Nullam lorem urna, tempus eget mollis et, dapibus ac sem. Suspendisse gravida ornare pulvinar. Vestibulum luctus ex in egestas fringilla.</p>
    <div class="abs feat" style="left:144px;top:2152px"><div class="feat-icon"><svg viewBox="0 0 24 24"><path d="M2 20V4h2v14h18v2zm4-4-1.4-1.4L10 9.2l3 3 5.6-5.6L20 8l-7 7-3-3z"/></svg></div><div><h4>Sed augue orci</h4><p>Nulla in lorem at massa pellentesque posuere. Nulla tristique posuere molestie. Aliquam erat volutpat.</p></div></div>
    <div class="abs feat" style="left:144px;top:2248px"><div class="feat-icon"><svg viewBox="0 0 24 24"><path d="M6 10V8a6 6 0 0 1 12 0v2h1v12H5V10zm3 0h6V8a3 3 0 0 0-6 0z"/></svg></div><div><h4>Aliquam consectetur</h4><p>Nulla in lorem at massa pellentesque posuere. Nulla tristique posuere molestie. Aliquam erat volutpat.</p></div></div>
    <div class="abs feat" style="left:144px;top:2344px"><div class="feat-icon"><svg viewBox="0 0 24 24"><path d="M11 3a9 9 0 1 0 9 10h-9zm2-1v9h9a9 9 0 0 0-9-9z"/></svg></div><div><h4>Proin eget congue</h4><p>Nulla in lorem at massa pellentesque posuere. Nulla tristique posuere molestie. Aliquam erat volutpat.</p></div></div>
    <div class="abs shot" style="left:615px;top:2077px;width:441px;height:241px"><div role="img" aria-label="Product import wizard screenshot"></div></div>
  </section>

  <!-- pricing -->
  <section>
    <h2 class="abs price-title">Simple, transparent pricing.</h2>
    <p class="abs price-sub">Always know what you'll Pay</p>

    <div class="abs card" style="left:144px">
      <h3>Vestibulum</h3>
      <p class="blurb">Pellentesque a imperdiet dolor, et auctor est. Fusce sollicitudin lorem et luctus volutpat.</p>
      <div class="price">$49 <small>/ mo</small></div>
      <div class="rule"></div>
      <ul>
        <li><svg viewBox="0 0 12 12"><path d="M1 6l3 3 7-7"/></svg>Proin placerat dapibus</li>
        <li><svg viewBox="0 0 12 12"><path d="M1 6l3 3 7-7"/></svg>Maecenas vel tortor accumsan</li>
        <li><svg viewBox="0 0 12 12"><path d="M1 6l3 3 7-7"/></svg>Aenean facilisis tincidunt</li>
      </ul>
      <a class="btn">Sign Up</a>
    </div>

    <div class="abs card" style="left:452px">
      <h3>Praesent</h3>
      <p class="blurb">Pellentesque a imperdiet dolor, et auctor est. Fusce sollicitudin lorem et luctus volutpat.</p>
      <div class="price">$99 <small>/ mo</small></div>
      <div class="rule"></div>
      <ul>
        <li><svg viewBox="0 0 12 12"><path d="M1 6l3 3 7-7"/></svg>Proin placerat dapibus</li>
        <li><svg viewBox="0 0 12 12"><path d="M1 6l3 3 7-7"/></svg>Maecenas vel tortor accumsan</li>
        <li><svg viewBox="0 0 12 12"><path d="M1 6l3 3 7-7"/></svg>Aenean facilisis tincidunt</li>
      </ul>
      <a class="btn">Sign Up</a>
    </div>

    <div class="abs card" style="left:759px">
      <h3>Fusce vitae</h3>
      <p class="blurb">Pellentesque a imperdiet dolor, et auctor est. Fusce sollicitudin lorem et luctus volutpat.</p>
      <div class="price">$199 <small>/ mo</small></div>
      <div class="rule"></div>
      <ul>
        <li><svg viewBox="0 0 12 12"><path d="M1 6l3 3 7-7"/></svg>Proin placerat dapibus</li>
        <li><svg viewBox="0 0 12 12"><path d="M1 6l3 3 7-7"/></svg>Maecenas vel tortor accumsan</li>
        <li><svg viewBox="0 0 12 12"><path d="M1 6l3 3 7-7"/></svg>Aenean facilisis tincidunt</li>
      </ul>
      <a class="btn">Sign Up</a>
    </div>
  </section>

  <!-- contact -->
  <section>
    <h2 class="abs contact-title">Contact us</h2>
    <p class="abs contact-sub">Got any questions? Don't hesitate to reach out.</p>
    <label class="abs label" style="left:319px;top:3454px">Full Name</label>
    <div class="abs field" style="left:319px;top:3480px;width:562px;height:46px">Jane Doe</div>
    <label class="abs label" style="left:319px;top:3558px">Email Address</label>
    <div class="abs field" style="left:319px;top:3584px;width:273px;height:46px">jane.doe@mail.com</div>
    <label class="abs label" style="left:606px;top:3558px">Phone (Optional)</label>
    <div class="abs field" style="left:606px;top:3584px;width:275px;height:46px">(123) 456-7890</div>
    <label class="abs label" style="left:319px;top:3662px">Your Message</label>
    <div class="abs field" style="left:319px;top:3688px;width:562px;height:142px"></div>
    <a class="abs send">SEND MESSAGE</a>
  </section>

  <!-- call to action -->
  <section>
    <h2 class="abs cta-title">Ready to get started?</h2>
    <p class="abs cta-sub" style="top:4176px;display:none"></p>
    <p class="abs cta-sub" style="top:4176px;visibility:hidden">.</p>
    <p class="abs cta-sub" style="top:4172px;display:none"></p>
    <p class="abs cta-sub" style="top:4176px;display:none"></p>
    <p class="abs cta-sub" style="top:4176px;display:none"></p>
    <p class="abs cta-sub" style="top:4180px;display:none"></p>
    <p class="abs cta-sub" style="top:4228px;display:none"></p>
    <p class="abs cta-sub" style="top:4226px;display:none"></p>
    <p class="abs cta-sub" style="top:4226px;display:none"></p>
    <p class="abs cta-sub" style="top:4226px;display:none"></p>
    <p class="abs cta-sub" style="top:4226px">Contact us or sign up now.</p>
    <a class="abs cta-btn" style="left:431px;top:4290px;background:var(--navy)">GET STARTED</a>
    <a class="abs cta-btn" style="left:606px;top:4290px;background:var(--sky)">CONTACT US</a>
  </section>

  <!-- footer -->
  <footer>
    <p class="abs foot-text" style="left:144px;top:4459px">Copyright © 2020 TenaPod.</p>
    <p class="abs foot-text" style="left:144px;top:4491px">All rights reserved.</p>
    <span class="abs social" style="left:144px" aria-label="social link"></span>
    <span class="abs social" style="left:180px" aria-label="social link"></span>
    <span class="abs social" style="left:216px" aria-label="social link"></span>

    <a class="abs foot-text" style="left:700px;top:4459px">Product</a>
    <a class="abs foot-text" style="left:700px;top:4491px">Features</a>
    <a class="abs foot-text" style="left:700px;top:4523px">Pricing</a>
    <a class="abs foot-text" style="left:700px;top:4555px">Tour</a>

    <a class="abs foot-text" style="left:827px;top:4459px">Company</a>
    <a class="abs foot-text" style="left:827px;top:4491px">About</a>
    <a class="abs foot-text" style="left:827px;top:4523px">Team</a>
    <a class="abs foot-text" style="left:827px;top:4555px">Blog</a>

    <a class="abs foot-text" style="left:956px;top:4459px">Legal</a>
    <a class="abs foot-text" style="left:956px;top:4491px">Terms of Service</a>
    <a class="abs foot-text" style="left:956px;top:4523px">Privacy Policy</a>
    <a class="abs foot-text" style="left:956px;top:4555px">GDPR Policy</a>
  </footer>

</div>
</body>
</html>
```